Bright Path Trading
Business Cards and Stationary
Project: Bright Path Trading
Bright Path Trading -
Creative Brief
Modern
Rob and Kara Halvorsen, Owners
47 Elmcrest Road Northampton, MA 01384
rob@brightpathtrading.com
www.brightpathtrading.com
Please put Kara's email underneath Rob's email: kara@brightpathtrading.com

```html
<!DOCTYPE html>
<html lang="en">
<head>
<meta charset="utf-8">
<title>Bright Path Trading – Stationery</title>
<link rel="stylesheet" href="https://fonts.googleapis.com/css2?family=Lato:wght@400;700;900&display=swap">
<style>
  :root {
    --green: #87a24c;
    --green-dark: #6f8a3a;
    --orange: #d4622a;
    --grey-card: #a9abae;
    --brand: #7b2220;
    --paper: #ffffff;
    --paper-shade: #ededed;
    --mark-faint: #e6e8dc;
    --ink: #5a5a5a;
  }
  * { box-sizing: border-box; margin: 0; padding: 0; }
  html, body { width: 1200px; height: 717px; overflow: hidden; background: #fff; }
  body { position: relative; font-family: "Lato", Arial, sans-serif; color: var(--ink); }

  .piece {
    position: absolute;
    overflow: hidden;
    background: linear-gradient(135deg, var(--paper) 0%, var(--paper) 45%, var(--paper-shade) 100%);
    box-shadow: 0 0 0 1px #d6d6d6;
  }
  .brand-name {
    position: absolute;
    font-weight: 900;
    color: var(--brand);
    letter-spacing: -0.2px;
    white-space: nowrap;
    display: flex; align-items: center; gap: 6px;
    line-height: 1.2;
  }
  .brand-dot { display: inline-block; border-radius: 50%; background: var(--green); flex: none; }
  .faint-mark { position: absolute; border-radius: 50%; border: 10px solid var(--mark-faint); }
  .footer-band { position: absolute; left: 0; bottom: 0; width: 100%; }
  .footer-text {
    position: absolute; left: 0; width: 100%; text-align: center;
    color: #fff; line-height: 1.45;
  }

  /* Letterhead */
  .letterhead { left: 24px; top: 36px; width: 468px; height: 648px; }
  .letterhead .brand-name { left: 26px; top: 40px; font-size: 22px; }
  .letterhead .brand-dot { width: 12px; height: 12px; }
  .letterhead .faint-mark { left: 150px; top: 210px; width: 190px; height: 190px; }
  .letterhead .footer-band { height: 80px; }
  .letterhead .footer-text { bottom: 10px; font-size: 6.5px; }

  /* Business cards */
  .card { width: 192px; height: 120px; }
  .card-front { left: 533px; top: 67px; }
  .card-front .brand-name { left: 10px; top: 12px; font-size: 10px; gap: 4px; }
  .card-front .brand-dot { width: 6px; height: 6px; }
  .card-front .owners {
    position: absolute; right: 10px; top: 32px;
    text-align: right; font-size: 6px; line-height: 1.4; white-space: nowrap;
  }
  .card-front .owners strong { color: var(--brand); font-weight: 700; }
  .card-front .footer-band { height: 50px; }
  .card-front .footer-text { bottom: 6px; font-size: 4.6px; }

  .card-back { display: flex; align-items: center; justify-content: center; box-shadow: none; }
  .card-back .back-mark { width: 46px; height: 46px; border-radius: 50%; border: 4px solid currentColor; }
  .card-orange { left: 751px; top: 67px; background: var(--orange); color: #fff; }
  .card-grey   { left: 972px; top: 67px; background: var(--grey-card); color: #fff; }
  .card-white-grey { left: 533px; top: 216px; color: #b9bbbd; box-shadow: 0 0 0 1px #d6d6d6; }
  .card-green  { left: 751px; top: 216px; background: var(--green); color: #fff; }
  .card-white-green { left: 972px; top: 216px; background: #fff; color: var(--green); box-shadow: 0 0 0 1px #d6d6d6; }

  /* Envelope */
  .envelope { left: 533px; top: 379px; width: 636px; height: 305px; }
  .envelope .flap { position: absolute; left: 0; top: 0; width: 100%; height: 110px; }
  .envelope .flap-mark { position: absolute; left: 306px; top: 22px; width: 24px; height: 24px; border-radius: 50%; border: 3px solid #fff; }
  .envelope .brand-name { left: 24px; top: 150px; font-size: 21px; }
  .envelope .brand-dot { width: 11px; height: 11px; }
  .envelope .faint-mark { left: 470px; top: 150px; width: 120px; height: 120px; border-width: 8px; }
  .envelope .footer-band { height: 48px; }
  .envelope .footer-text { bottom: 10px; font-size: 6px; }
</style>
</head>
<body>

  <section class="piece letterhead">
    <div class="brand-name"><span class="brand-dot"></span>Bright Path Trading</div>
    <div class="faint-mark"></div>
    <svg class="footer-band" viewBox="0 0 468 80" preserveAspectRatio="none">
      <path d="M0 22 Q234 -6 468 22 L468 80 L0 80 Z" fill="var(--orange)"/>
      <path d="M0 27 Q234 0 468 27 L468 80 L0 80 Z" fill="var(--green)"/>
    </svg>
    <div class="footer-text">
      47 Elmcrest Road Northampton, MA 01384<br>
      Phone 413.555.0148 &nbsp; Fax 413.555.0149<br>
      rob@brightpathtrading.com &nbsp; kara@brightpathtrading.com<br>
      www.brightpathtrading.com
    </div>
  </section>

  <section class="piece card card-front">
    <div class="brand-name"><span class="brand-dot"></span>Bright Path Trading</div>
    <div class="owners"><strong>Rob and Kara Halvorsen</strong><br>Owners</div>
    <svg class="footer-band" viewBox="0 0 192 50" preserveAspectRatio="none">
      <path d="M0 10 Q96 -4 192 10 L192 50 L0 50 Z" fill="var(--orange)"/>
      <path d="M0 13 Q96 0 192 13 L192 50 L0 50 Z" fill="var(--green)"/>
    </svg>
    <div class="footer-text">
      47 Elmcrest Road Northampton, MA 01384<br>
      rob@brightpathtrading.com<br>
      kara@brightpathtrading.com<br>
      www.brightpathtrading.com
    </div>
  </section>

  <section class="piece card card-back card-orange"><div class="back-mark"></div></section>
  <section class="piece card card-back card-grey"><div class="back-mark"></div></section>
  <section class="piece card card-back card-white-grey"><div class="back-mark"></div></section>
  <section class="piece card card-back card-green"><div class="back-mark"></div></section>
  <section class="piece card card-back card-white-green"><div class="back-mark"></div></section>

  <section class="piece envelope">
    <svg class="flap" viewBox="0 0 636 110" preserveAspectRatio="none">
      <path d="M0 0 L636 0 L636 58 Q318 112 0 58 Z" fill="var(--orange)"/>
      <path d="M0 0 L636 0 L636 54 Q318 106 0 54 Z" fill="var(--green)"/>
    </svg>
    <div class="flap-mark"></div>
    <div class="brand-name"><span class="brand-dot"></span>Bright Path Trading</div>
    <div class="faint-mark"></div>
    <svg class="footer-band" viewBox="0 0 636 48" preserveAspectRatio="none">
      <path d="M0 14 Q318 -4 636 14 L636 48 L0 48 Z" fill="var(--orange)"/>
      <path d="M0 18 Q318 0 636 18 L636 48 L0 48 Z" fill="var(--green)"/>
    </svg>
    <div class="footer-text">47 Elmcrest Road Northampton, MA 01384</div>
  </section>

</body>
</html>
```